Promo Flyer to put in prize bags at carnival

I am owner of Copper & Lark Hair Salon located in Gahanna, OH. I’m sponsoring a community carnival when I will be putting flyers in all attendees prize bags. This flyer will communicate details of my salon on one side (picture of me, logo, description of business, address, website, email, phone #) and the other side will showcase and a 50% discount for first time customers. Flyer can be 5” x 7” or greater

Side 1 details:
-Logo will be attached to this brief
-picture of me will be attached to this brief
-address: 2561 W. Pellward Ave, Suite 17, Gahanna, OH, 43230
-website: clhairstudio.example
-email: Dorian.welby@clhairstudio.example
-phone: 614-52-BOOKS (26657)

Side 2 details:
-‘Guess what? You get 50% off your 1st service at Copper & Lark Hair Salon.’
-‘Expires 7/31/2018’
-Hair | Fashion | Photography
-Visit clhairstudio.example to book your service
-must present this flyer at time of service to receive discount

Hair And Beauty

Other font styles liked:
• Inoxida

Colors
3176b5
000000
ffffff

Must have
• 2 sides
• Color scheme to match logo

```html
<!DOCTYPE html>
<html lang="en">
<head>
<meta charset="utf-8">
<title>Copper &amp; Lark Hair Salon – Carnival Flyer</title>
<link rel="stylesheet" href="https://fonts.googleapis.com/css2?family=Tinos:ital,wght@0,400;0,700;1,400&display=swap">
<style>
  :root {
    --blue: #3176b5;
    --sky: #4bbfea;
    --ink: #000000;
    --paper: #ffffff;
    --panel-light: #f2f2f2;
    --panel-dark: #2a2a2a;
    --muted: #d9d9d9;
    --stage: #e6e5e3;
    --photo-deep: #1f3440;
    --photo-mid: #5c6a72;
    --photo-light: #b7b2a8;
  }
  * { box-sizing: border-box; margin: 0; padding: 0; }
  html, body {
    width: 870px; height: 1200px; overflow: hidden;
    background: var(--stage);
    font-family: "Tinos", "Times New Roman", serif;
  }
  .canvas { position: relative; width: 870px; height: 1200px; }

  .flyer-side {
    position: absolute; left: 93px;
    width: 700px; height: 501px;
    transform: scale(.973); transform-origin: top left;
    overflow: hidden;
    box-shadow: 0 6px 14px rgba(0,0,0,.35);
  }
  .flyer-side--front { top: 72px; }
  .flyer-side--back  { top: 655px; }

  .photo { position: absolute; top: 0; height: 100%; }
  .flyer-side--front .photo {
    left: 0; width: 344px;
    background: linear-gradient(160deg, var(--photo-light) 0%, var(--photo-mid) 45%, var(--photo-deep) 100%);
  }
  .flyer-side--back .photo {
    left: 398px; width: 302px;
    background: linear-gradient(200deg, #3a2a22 0%, var(--photo-deep) 55%, #111 100%);
  }
  .corner-shape { position: absolute; }

  /* front info panel */
  .info-panel {
    position: absolute; left: 344px; top: 0; width: 356px; height: 100%;
    background: radial-gradient(ellipse at 55% 55%, #555 0%, var(--panel-dark) 55%, #151515 100%);
    color: var(--paper); text-align: center;
  }
  .brand-name {
    font-size: 38px; font-weight: 400; line-height: 1; white-space: nowrap;
  }
  .info-panel .brand-name { position: absolute; top: 158px; left: 0; width: 100%; color: var(--paper); }
  .tagline {
    display: flex; align-items: center; justify-content: center; gap: 6px;
    font-size: 13px; font-style: italic; line-height: 1; white-space: nowrap;
  }
  .tagline::before, .tagline::after { content: ""; width: 22px; height: 1px; background: currentColor; }
  .info-panel .tagline { position: absolute; top: 202px; left: 0; width: 100%; color: var(--muted); }
  .about {
    position: absolute; top: 248px; left: 20px; width: 322px;
    font-size: 13px; line-height: 19px; text-align: left; color: #e6e6e6;
  }
  .phone-tab {
    position: absolute; left: 330px; top: 342px; width: 10px; height: 55px; background: var(--sky);
  }
  .phone-band {
    position: absolute; left: 20px; top: 342px; width: 336px; height: 55px;
    background: linear-gradient(90deg, var(--sky), var(--blue));
    display: flex; align-items: center; justify-content: center; gap: 12px;
    font-size: 21px; font-weight: 700; color: var(--paper);
  }
  .social-row {
    position: absolute; top: 416px; left: 0; width: 100%;
    display: flex; justify-content: center; gap: 10px;
  }
  .social-dot { width: 24px; height: 24px; border: 1px solid var(--paper); border-radius: 50%; }
  .contact-line { position: absolute; left: 0; width: 100%; font-size: 11px; white-space: nowrap; }
  .contact-line--web { top: 456px; color: var(--sky); }
  .contact-line--address { top: 473px; color: #e0e0e0; }

  /* back offer panel */
  .offer-panel {
    position: absolute; left: 0; top: 0; width: 398px; height: 100%;
    background: var(--panel-light); color: var(--ink);
  }
  .offer-panel .brand-name { position: absolute; top: 102px; left: 0; width: 360px; text-align: center; }
  .offer-panel .tagline { position: absolute; top: 150px; left: 0; width: 360px; color: var(--ink); }
  .offer-kicker { position: absolute; top: 194px; left: 30px; font-size: 21px; color: var(--sky); }
  .offer-headline { position: absolute; top: 224px; left: 30px; width: 360px; font-size: 22px; line-height: 32px; }
  .offer-divider { position: absolute; top: 299px; left: 28px; width: 362px; border-top: 1.5px dotted var(--ink); }
  .offer-expiry { position: absolute; top: 318px; left: 33px; font-size: 11px; }
  .offer-services { position: absolute; top: 355px; left: 33px; font-size: 20px; letter-spacing: .3px; white-space: nowrap; }
  .booking-band {
    position: absolute; left: 0; top: 401px; width: 388px; height: 56px;
    background: linear-gradient(90deg, #111 0%, #3a3a3a 50%, #111 100%);
    color: var(--paper); font-size: 18px; white-space: nowrap;
    display: flex; align-items: center; justify-content: center;
  }
  .booking-band strong { font-weight: 700; margin: 0 4px; }
  .booking-tab { position: absolute; left: 398px; top: 401px; width: 20px; height: 56px; background: var(--ink); }
  .offer-terms { position: absolute; top: 470px; left: 0; width: 398px; text-align: center; font-size: 10px; font-weight: 700; white-space: nowrap; }
</style>
</head>
<body>
<main class="canvas">

  <section class="flyer-side flyer-side--front" aria-label="Salon details side">
    <div class="photo" role="img" aria-label="Photo of the salon owner in a teal suit and sunglasses, standing on a city street"></div>
    <svg class="corner-shape" style="left:0;top:0" width="330" height="170" viewBox="0 0 330 170">
      <defs>
        <linearGradient id="blueCorner" x1="0" y1="0" x2="1" y2="0">
          <stop offset="0" stop-color="#4bbfea"/><stop offset="1" stop-color="#3176b5"/>
        </linearGradient>
      </defs>
      <polygon points="0,0 322,0 0,162" fill="url(#blueCorner)"/>
    </svg>
    <div class="phone-tab"></div>
    <div class="info-panel">
      <h1 class="brand-name">Copper &amp; Lark</h1>
      <p class="tagline">An experience out of this world</p>
      <p class="about">Membership salon offering unlimited hair services and exclusive image consulting tailored to who you are and where you're going. Join a community where being set apart is a way of life... Copper &amp; Lark.</p>
      <div class="phone-band">
        <svg width="24" height="24" viewBox="0 0 24 24" aria-hidden="true">
          <circle cx="12" cy="12" r="11" fill="none" stroke="#fff" stroke-width="1.6"/>
          <path d="M8.2 6.5c.5-.4 1.1-.3 1.4.2l1 1.7c.3.5.2 1-.2 1.4l-.7.6c.6 1.3 1.6 2.4 2.9 3l.6-.7c.4-.4.9-.5 1.4-.2l1.7 1c.5.3.6.9.2 1.4l-.8.9c-.6.6-1.5.8-2.3.4-2.7-1.2-4.8-3.3-6-6-.4-.8-.2-1.7.4-2.3z" fill="#fff"/>
        </svg>
        <span>614-52-BOOKS (26657)</span>
      </div>
      <div class="social-row" aria-label="Social media">
        <span class="social-dot"></span><span class="social-dot"></span>
      </div>
      <p class="contact-line contact-line--web">dorian.welby@clhairstudio.example&nbsp;|&nbsp; clhairstudio.example</p>
      <p class="contact-line contact-line--address">2561 W. Pellward Ave, Suite 17, Gahanna, OH, 43230</p>
    </div>
  </section>

  <section class="flyer-side flyer-side--back" aria-label="Discount offer side">
    <div class="photo" role="img" aria-label="Photo of the salon owner in a teal suit standing in a doorway"></div>
    <svg class="corner-shape" style="left:555px;top:400px" width="145" height="101" viewBox="0 0 145 101">
      <polygon points="145,5 145,101 5,101" fill="#fff"/>
    </svg>
    <div class="offer-panel">
      <svg class="corner-shape" style="left:0;top:0" width="190" height="130" viewBox="0 0 190 130">
        <defs>
          <linearGradient id="darkCorner" x1="0" y1="0" x2="1" y2="1">
            <stop offset="0" stop-color="#111"/><stop offset=".6" stop-color="#555"/><stop offset="1" stop-color="#222"/>
          </linearGradient>
        </defs>
        <polygon points="0,0 186,0 0,126" fill="url(#darkCorner)"/>
      </svg>
      <h2 class="brand-name">Copper &amp; Lark</h2>
      <p class="tagline">An experience out of this world</p>
      <p class="offer-kicker">Guess what?</p>
      <p class="offer-headline">You get 50% off &nbsp;your 1st service at Copper &amp; Lark Hair Salon.</p>
      <div class="offer-divider"></div>
      <p class="offer-expiry">Expires 7/31/2018</p>
      <p class="offer-services">HAIR | FASHION | PHOTOGRAPHY</p>
      <div class="booking-band">Visit <strong>clhairstudio.example</strong> to book your service</div>
      <p class="offer-terms">must present this flyer at time of service to receive discount</p>
    </div>
    <div class="booking-tab"></div>
  </section>

</main>
</body>
</html>
```